professional business card

Professional business card with logo on one side, and underneath logo list:
- power
-data
-fibre optic
-isolar

On other side:
Marcus Trent
Owner
MOB 0492 738 204
marcus@vorpa.com.au
www.vorpaelectrical.com.au

Please edit logo to just leave VORPA

```html
<!DOCTYPE html>
<html lang="en">
<head>
<meta charset="UTF-8">
<title>VORPA Business Card</title>
<link href="https://fonts.googleapis.com/css2?family=Lato:wght@300;400&display=swap" rel="stylesheet">
<style>
  :root {
    --stage: #2b2e33;
    --card: #0b0b0c;
    --teal: #1fa3a8;
    --name-grey: #a9abae;
    --text-grey: #8c8f93;
    --band-text: #e8f7f7;
  }
  * { margin: 0; padding: 0; box-sizing: border-box; }
  html, body {
    width: 1200px;
    height: 900px;
    overflow: hidden;
    background: var(--stage);
    font-family: "Lato", sans-serif;
  }
  .stage {
    width: 1200px;
    height: 900px;
    display: flex;
    align-items: center;
    justify-content: center;
  }
  .card {
    position: relative;
    width: 1000px;
    height: 570px;
    background: var(--card);
    border-radius: 40px;
    overflow: hidden;
    box-shadow: 0 24px 60px rgba(0,0,0,0.45);
  }
  .brand {
    position: absolute;
    right: 80px;
    top: 80px;
    display: flex;
    align-items: center;
    gap: 18px;
    font-weight: 400;
    font-size: 64px;
    line-height: 1;
    letter-spacing: 3px;
    color: var(--teal);
  }
  .brand-square {
    width: 34px;
    height: 34px;
    background: var(--teal);
    flex: none;
  }
  .person-name {
    position: absolute;
    left: 60px;
    top: 178px;
    font-weight: 300;
    font-size: 40px;
    letter-spacing: 1px;
    text-transform: uppercase;
    color: var(--name-grey);
  }
  .person-role {
    position: absolute;
    left: 60px;
    top: 228px;
    font-weight: 400;
    font-size: 19px;
    text-transform: uppercase;
    color: var(--teal);
  }
  .divider {
    position: absolute;
    left: 150px;
    right: 0;
    top: 240px;
    height: 3px;
    background: var(--teal);
  }
  .contacts {
    position: absolute;
    left: 60px;
    top: 280px;
    list-style: none;
  }
  .contacts li {
    display: flex;
    align-items: center;
    gap: 14px;
    height: 40px;
    font-size: 22px;
    font-weight: 400;
    color: var(--text-grey);
  }
  .contacts svg { width: 20px; height: 20px; flex: none; }
  .services-band {
    position: absolute;
    left: 0;
    right: 0;
    bottom: 0;
    height: 110px;
    background: var(--teal);
    display: flex;
    align-items: center;
    padding-left: 60px;
    gap: 22px;
    font-size: 28px;
    font-weight: 400;
    text-transform: uppercase;
    color: var(--band-text);
  }
  .services-band .sep { font-weight: 300; }
</style>
</head>
<body>
<main class="stage">
  <section class="card">
    <div class="brand"><span class="brand-square"></span><span class="brand-name">VORPA</span></div>

    <h1 class="person-name">Marcus Trent</h1>
    <p class="person-role">Owner</p>
    <div class="divider"></div>

    <ul class="contacts">
      <li>
        <svg viewBox="0 0 20 20" aria-hidden="true"><rect x="5" y="1" width="10" height="18" rx="2" fill="none" stroke="#1fa3a8" stroke-width="2"/><circle cx="10" cy="15.5" r="1.2" fill="#1fa3a8"/></svg>
        0492 738 204
      </li>
      <li>
        <svg viewBox="0 0 20 20" aria-hidden="true"><rect x="1" y="4" width="18" height="12" rx="1.5" fill="#1fa3a8"/><path d="M2 5 L10 11 L18 5" fill="none" stroke="#0b0b0c" stroke-width="1.6"/></svg>
        marcus@vorpa.com.au
      </li>
      <li>
        <svg viewBox="0 0 20 20" aria-hidden="true"><circle cx="10" cy="10" r="8.5" fill="none" stroke="#1fa3a8" stroke-width="2"/><ellipse cx="10" cy="10" rx="3.5" ry="8.5" fill="none" stroke="#1fa3a8" stroke-width="1.5"/><line x1="1.5" y1="10" x2="18.5" y2="10" stroke="#1fa3a8" stroke-width="1.5"/></svg>
        www.vorpaelectrical.com.au
      </li>
    </ul>

    <div class="services-band">
      <span>Power</span><span class="sep">|</span>
      <span>Data</span><span class="sep">|</span>
      <span>Fibre Optic</span><span class="sep">|</span>
      <span>Solar</span>
    </div>
  </section>
</main>
</body>
</html>
```